Heating and Cooling Company mobile website

We need a website specifically designed for a viewing on a mobile device.

We serve the northern New Jersey heating, cooling and electrical residential market.

The goal is the drive traffic to the site by using Brindle Pay Per click. People will be searching for an HVAC contractor, and they land on our page. They need to get key info quickly without all the clutter of a desktop type of site.

Target Market(s)

Homeowners

Industry/Entity Type

Hvac

Coding

Coded - Design and coding required

Number of Pages Required

5+ page

Font styles to use
Serif

Requirements
Must have
• View attachments to see samples of the desktop version. It must have a similar color scheme
• The copy of the website is also attached
Nice to have
• Would like it to have a sort of Quello feel to it. Make it seem like its an app that people are using and that its exciting to be on the website. It would be nice to have a page where customers can book appointments

```html
<!DOCTYPE html>
<html lang="en">
<head>
<meta charset="UTF-8">
<title>Heating &amp; Cooling – Mobile Home</title>
<link rel="stylesheet" href="https://fonts.googleapis.com/css2?family=Montserrat:wght@700&display=swap">
<style>
  :root {
    --navy: #27304f;
    --navy-deep: #161c33;
    --cream: #f1e7cf;
    --paper: #ece6e6;
    --maroon: #8e1426;
    --orange: #ee7a22;
    --label: #2c3350;
    --shadow: rgba(60, 50, 50, 0.28);
    --sand-light: #d9ccb9;
    --sand-dark: #8f7f6c;
  }
  html, body {
    margin: 0;
    padding: 0;
    width: 752px;
    height: 1200px;
    overflow: hidden;
    background: var(--paper);
  }
  .screen {
    position: relative;
    width: 752px;
    height: 1200px;
    background: var(--paper);
    font-family: "Montserrat", Arial, sans-serif;
  }
  .header-band {
    position: absolute;
    top: 0; left: 0;
    width: 752px;
    height: 200px;
  }
  .service-badge {
    position: absolute;
    width: 264px;
    height: 244px;
    box-sizing: border-box;
    border: 8px solid var(--orange);
    border-radius: 34px;
    background: var(--maroon);
    display: flex;
    align-items: center;
    justify-content: center;
  }
  .service-badge svg {
    width: 120px;
    height: 120px;
  }
  .badge-shadow {
    position: absolute;
    width: 190px;
    height: 22px;
    border-radius: 50%;
    background: radial-gradient(ellipse at center, var(--shadow) 0%, rgba(60,50,50,0) 70%);
  }
  .service-label {
    position: absolute;
    width: 376px;
    margin: 0;
    text-align: center;
    color: var(--label);
    font-size: 28px;
    line-height: 34px;
    font-weight: 700;
    letter-spacing: 0.3px;
    white-space: nowrap;
  }
  .col-left  .service-badge { left: 58px; }
  .col-right .service-badge { left: 431px; }
  .col-left  .badge-shadow  { left: 95px; }
  .col-right .badge-shadow  { left: 468px; }
  .col-left  .service-label { left: 20px; }
  .col-right .service-label { left: 376px; }
  .row-top .service-badge    { top: 88px; }
  .row-top .badge-shadow     { top: 356px; }
  .row-top .service-label    { top: 412px; }
  .row-bottom .service-badge { top: 542px; }
  .row-bottom .badge-shadow  { top: 806px; }
  .row-bottom .service-label { top: 864px; }
  .family-photo {
    position: absolute;
    left: 0; top: 954px;
    width: 752px;
    height: 246px;
    background: linear-gradient(180deg, var(--sand-light) 0%, #cdbfa9 45%, var(--sand-dark) 100%);
  }
</style>
</head>
<body>
<main class="screen">

  <svg class="header-band" viewBox="0 0 752 200" aria-hidden="true">
    <path d="M0 0 H376 V196 Q200 150 0 158 Z" fill="var(--navy)"/>
    <path d="M376 0 H752 V158 Q552 150 376 196 Z" fill="var(--navy-deep)"/>
    <path d="M190 0 Q310 6 376 30 Q442 6 562 0 Z" fill="var(--cream)"/>
  </svg>

  <a class="service-tile col-left row-top">
    <span class="service-badge">
      <svg viewBox="0 0 60 60" aria-hidden="true">
        <circle cx="30" cy="30" r="11" fill="var(--cream)"/>
        <g stroke="var(--cream)" stroke-width="3" stroke-linecap="round">
          <line x1="30" y1="6" x2="30" y2="12"/><line x1="30" y1="48" x2="30" y2="54"/>
          <line x1="6" y1="30" x2="12" y2="30"/><line x1="48" y1="30" x2="54" y2="30"/>
        </g>
      </svg>
    </span>
    <span class="badge-shadow"></span>
    <p class="service-label">HEATING</p>
  </a>

  <a class="service-tile col-right row-top">
    <span class="service-badge">
      <svg viewBox="0 0 60 60" aria-hidden="true">
        <g stroke="var(--cream)" stroke-width="3.5" stroke-linecap="round">
          <line x1="30" y1="8" x2="30" y2="52"/>
          <line x1="11" y1="19" x2="49" y2="41"/>
          <line x1="11" y1="41" x2="49" y2="19"/>
        </g>
      </svg>
    </span>
    <span class="badge-shadow"></span>
    <p class="service-label">AIR CONDITIONING</p>
  </a>

  <a class="service-tile col-left row-bottom">
    <span class="service-badge">
      <svg viewBox="0 0 60 60" aria-hidden="true">
        <g stroke="var(--cream)" stroke-width="3.5" stroke-linecap="round">
          <line x1="14" y1="18" x2="46" y2="18"/>
          <line x1="14" y1="30" x2="46" y2="30"/>
          <line x1="14" y1="42" x2="46" y2="42"/>
        </g>
      </svg>
    </span>
    <span class="badge-shadow"></span>
    <p class="service-label">OTHER SERVICES</p>
  </a>

  <a class="service-tile col-right row-bottom">
    <span class="service-badge">
      <svg viewBox="0 0 60 60" aria-hidden="true">
        <path d="M12 30 L30 14 L48 30 V48 H12 Z" fill="none" stroke="var(--cream)" stroke-width="3.5" stroke-linejoin="round"/>
      </svg>
    </span>
    <span class="badge-shadow"></span>
    <p class="service-label">WHO WE SERVICE</p>
  </a>

  <div class="family-photo" role="img" aria-label="Sepia photo of a family walking hand in hand along a beach"></div>

</main>
</body>
</html>
```